Book Cover Design

Design with title UNWAVERING
Subtitle: Ways to Kindle the Spark of Resolve
Author Name: Carla Jean Morrow
Put DAILY MERIDIAN BESTSELLER at top
Shimmer design, see inspirational images attached

```html
<!DOCTYPE html>
<html lang="en">
<head>
<meta charset="UTF-8">
<title>Unwavering — Book Cover</title>
<link href="https://fonts.googleapis.com/css2?family=Anton&family=Archivo+Narrow:wght@700&family=Oswald:wght@500;700&display=swap" rel="stylesheet">
<style>
  :root {
    --stage: #4a4a4c;
    --ink: #111114;
    --shimmer-lilac: #c9b8e6;
    --shimmer-sky: #bfe3f0;
    --shimmer-pearl: #f1eef6;
    --shimmer-violet: #a99bd6;
    --shimmer-aqua: #9fd8e2;
    --echo: rgba(255, 255, 255, 0.7);
  }
  * { margin: 0; padding: 0; box-sizing: border-box; }
  html, body {
    width: 1200px;
    height: 958px;
    overflow: hidden;
    background: var(--stage);
  }
  .stage {
    width: 1200px;
    height: 958px;
    display: flex;
    align-items: center;
    justify-content: center;
  }
  .cover {
    position: relative;
    width: 600px;
    height: 900px;
    overflow: hidden;
    color: var(--ink);
  }
  .cover__shimmer {
    position: absolute;
    inset: 0;
    background:
      radial-gradient(ellipse 70% 40% at 20% 20%, var(--shimmer-sky), transparent 70%),
      radial-gradient(ellipse 60% 35% at 85% 45%, var(--shimmer-violet), transparent 70%),
      radial-gradient(ellipse 70% 30% at 30% 70%, var(--shimmer-aqua), transparent 70%),
      radial-gradient(ellipse 60% 30% at 70% 90%, var(--shimmer-lilac), transparent 70%),
      linear-gradient(160deg, var(--shimmer-pearl), var(--shimmer-lilac) 40%, var(--shimmer-pearl) 65%, var(--shimmer-sky));
  }
  .cover__content {
    position: absolute;
    inset: 0;
  }
  .bestseller {
    position: absolute;
    top: 52px;
    width: 100%;
    text-align: center;
    font-family: "Oswald", sans-serif;
    font-weight: 700;
    font-size: 22px;
    letter-spacing: 0.5px;
  }
  .title {
    position: absolute;
    top: 88px;
    width: 100%;
    text-align: center;
    font-family: "Anton", sans-serif;
    font-size: 112px;
    line-height: 1.2;
    letter-spacing: 1px;
  }
  .subtitle {
    position: absolute;
    top: 250px;
    width: 100%;
    text-align: center;
    font-family: "Archivo Narrow", sans-serif;
    font-weight: 700;
    font-size: 48px;
    line-height: 1.02;
    text-transform: uppercase;
  }
  .subtitle span { display: block; }
  .echo {
    position: absolute;
    left: 360px;
    top: 600px;
    font-family: "Oswald", sans-serif;
    font-weight: 700;
    color: var(--echo);
    line-height: 1;
    text-transform: uppercase;
  }
  .echo span { display: block; }
  .echo__sm { font-size: 20px; }
  .echo__md { font-size: 30px; }
  .echo__lg { font-size: 48px; margin-left: -10px; }
  .author {
    position: absolute;
    bottom: 72px;
    width: 100%;
    text-align: center;
    font-family: "Oswald", sans-serif;
    font-weight: 500;
    font-size: 30px;
    letter-spacing: 1px;
    text-transform: uppercase;
  }
</style>
</head>
<body>
<main class="stage">
  <article class="cover">
    <div class="cover__shimmer" role="img" aria-label="Iridescent holographic shimmer texture in lilac, sky blue and pearl"></div>
    <div class="cover__content">
      <p class="bestseller">DAILY MERIDIAN BESTSELLER</p>
      <h1 class="title">UNWAVERING</h1>
      <h2 class="subtitle">
        <span>Ways to</span>
        <span>Kindle</span>
        <span>the Spark</span>
        <span>of</span>
        <span>Resolve</span>
      </h2>
      <div class="echo" aria-hidden="true">
        <span class="echo__sm">Unwavering Unwavering</span>
        <span class="echo__md">Unwavering</span>
        <span class="echo__lg">Unwavering</span>
        <span class="echo__sm">Unwavering</span>
      </div>
      <p class="author">Carla Jean Morrow</p>
    </div>
  </article>
</main>
</body>
</html>
```